Corvane Agribusiness Consulting needs a Website Design.

We need a website design for a new company based in UK. Corvane offers agribusiness consulting and farm design services to farmers, smallholders and the wider agribusiness industry to assist clients in adopting more sustainable and regenerative production, processing and marketing practices.
Services are offered face-to-face and on a remote platform.
Services are offered in the UK and overseas.
We would like to see designs that reflect the natural environment, business and sustainability. Desired colours; green, blue, grey. The final design should communicate professionalism in the rural economy.
The design should be able to be customized by the client to make future changes and additions.
Target Market(s)
Farmers, smallholders, and the agricultural industry in UK and overseas.
Industry/Entity Type
Agribusiness
Number of Pages Required
4 page

```html
<!DOCTYPE html>
<html lang="en">
<head>
<meta charset="utf-8">
<title>Corvane Agribusiness Consulting</title>
<link href="https://fonts.googleapis.com/css2?family=Lato:wght@300;400;700&family=Oswald:wght@300;400&display=swap" rel="stylesheet">
<style>
  :root {
    --green: #8cc63f;
    --text-dark: #3a3a3a;
    --text-mid: #666666;
    --text-soft: #8a8a8a;
    --rule: #dcdcdc;
    --section-grey: #f6f6f6;
    --header-bg: #f8f9fa;
    --white: #ffffff;
  }
  * { margin: 0; padding: 0; box-sizing: border-box; }
  html, body { width: 1033px; height: 1200px; overflow: hidden; background: var(--white); }
  body { position: relative; font-family: "Lato", sans-serif; color: var(--text-mid); }
  .abs { position: absolute; }

  .site-header { left: 0; top: 0; width: 1033px; height: 71px; background: var(--header-bg); border-top: 2px solid var(--green); border-bottom: 1px solid #e4e4e4; }
  .brand-name { left: 151px; top: 19px; font-size: 23px; font-weight: 400; color: var(--green); line-height: 1; }
  .brand-tag { left: 151px; top: 43px; font-size: 12.5px; color: var(--text-dark); line-height: 1; }
  .main-nav a { position: absolute; top: 34px; font-size: 9.6px; color: #555; text-decoration: none; letter-spacing: 0.2px; line-height: 1; }
  .main-nav a.active { color: var(--green); }

  .hero { left: 0; top: 71px; width: 1033px; height: 375px;
    background: linear-gradient(180deg, #cfd4d9 0%, #dde1e5 35%, #a9b1ba 70%, #8ea27a 84%, #6f9a42 90%, #63903a 100%); }
  .hero-title { left: 0; top: 236px; width: 1008px; text-align: center; font-family: "Oswald", sans-serif; font-weight: 300; font-size: 30px; color: var(--white); letter-spacing: 0; text-shadow: 0 1px 3px rgba(0,0,0,0.35); line-height: 1; }
  .slider-tab { left: 478px; top: 420px; width: 74px; height: 26px; background: #e9e9e9; border-radius: 3px 3px 0 0; }
  .slider-tab span { position: absolute; top: 10px; width: 8px; height: 8px; border-radius: 50%; background: #333; }
  .slider-tab span.on { background: var(--white); border: 1px solid #bbb; }

  .services { left: 0; top: 446px; width: 1033px; height: 374px; background: var(--section-grey); }
  .section-title { font-weight: 300; font-size: 23px; color: #6a6a6a; text-align: center; line-height: 1; }
  .title-rule { height: 1px; background: var(--rule); }
  .service-card { top: 548px; width: 233px; height: 170px; background: var(--white); }
  .service-card h3 { position: absolute; top: 14px; width: 100%; text-align: center; font-weight: 400; font-size: 16px; color: #777; }
  .service-card h3.highlight { color: var(--green); }
  .service-photo { position: absolute; left: 15px; top: 47px; width: 202px; height: 104px; }
  .service-text { top: 731px; width: 233px; text-align: center; font-size: 10px; line-height: 12px; color: #8a8a8a; }

  .welcome-title { left: 0; top: 875px; width: 1033px; text-align: center; font-size: 23px; font-weight: 300; color: #777; line-height: 1; }
  .welcome-title strong { color: var(--green); font-weight: 400; }
  .welcome-text { left: 222px; top: 923px; width: 588px; text-align: center; font-family: Arial, sans-serif; font-size: 9.5px; line-height: 13px; color: #777; }
  .btn-about { left: 466px; top: 991px; width: 98px; height: 31px; border: 1px solid #ccc; background: var(--white); text-align: center; line-height: 29px; font-size: 10.5px; font-weight: 700; color: #777; letter-spacing: 0.8px; text-decoration: none; }

  .divider { left: 0; width: 1033px; height: 1px; background: var(--rule); }
  .social-circle { left: 494px; top: 1061px; width: 40px; height: 40px; border-radius: 50%; border: 2px solid #bdbdbd; background: var(--white); }
  .tweet-meta, .tweet-body { left: 0; width: 1028px; text-align: center; font-family: Arial, sans-serif; font-size: 9.5px; color: #888; line-height: 1; }
  .tweet-meta { top: 1111px; }
  .tweet-body { top: 1124px; }
  .tweet-body a { color: var(--green); text-decoration: none; }
  .copyright { left: 0; top: 1176px; width: 1028px; text-align: center; font-family: Arial, sans-serif; font-size: 8px; color: #999; line-height: 1; }
</style>
</head>
<body>
  <header class="abs site-header"></header>
  <div class="abs brand-name">Corvane</div>
  <div class="abs brand-tag">Agribusiness Consulting</div>
  <nav class="main-nav">
    <a class="active" href="#" style="left:551px">HOME</a>
    <a href="#" style="left:611px">ABOUT US</a>
    <a href="#" style="left:683px">WHAT WE DO</a>
    <a href="#" style="left:768px">SERVICES</a>
    <a href="#" style="left:835px">CONTACT</a>
  </nav>

  <section class="abs hero" role="img" aria-label="Photograph of a large oak tree in a green meadow under a cloudy sky"></section>
  <h1 class="abs hero-title">SOWING TRUST... REAPING HAPPINESS</h1>
  <div class="abs slider-tab">
    <span class="on" style="left:13px"></span>
    <span style="left:25px"></span>
    <span style="left:37px"></span>
    <span style="left:49px"></span>
  </div>

  <section class="abs services"></section>
  <div class="abs title-rule" style="left:151px; top:511px; width:279px"></div>
  <div class="abs title-rule" style="left:600px; top:511px; width:278px"></div>
  <h2 class="abs section-title" style="left:430px; top:497px; width:170px">What We Do</h2>

  <article class="abs service-card" style="left:151px">
    <h3 class="highlight">Consulting</h3>
    <div class="service-photo" role="img" aria-label="Photograph of a wooden farm gate opening onto rolling green fields" style="background: linear-gradient(180deg, #b7c0c8 0%, #93a878 40%, #7d9a52 100%);"></div>
  </article>
  <article class="abs service-card" style="left:398px">
    <h3>Production</h3>
    <div class="service-photo" role="img" aria-label="Photograph of a tray of white eggs with one brown egg" style="background: linear-gradient(180deg, #ece9e5 0%, #d9d4ce 100%);"></div>
  </article>
  <article class="abs service-card" style="left:646px">
    <h3>Marketing</h3>
    <div class="service-photo" role="img" aria-label="Photograph of round hay bales across a harvested golden field" style="background: linear-gradient(180deg, #c9a06a 0%, #d8ae72 50%, #c89656 100%);"></div>
  </article>

  <p class="abs service-text" style="left:151px">Lorem ipsum dolor sit amet, consectetur adipiscing elit, sed do eiusmod tempor incididunt ut labore et dolore magna aliqua.</p>
  <p class="abs service-text" style="left:398px">Lorem ipsum dolor sit amet, consectetur adipiscing elit, sed do eiusmod tempor incididunt ut labore et dolore magna aliqua.</p>
  <p class="abs service-text" style="left:646px">Lorem ipsum dolor sit amet, consectetur adipiscing elit, sed do eiusmod tempor incididunt ut labore et dolore magna aliqua.</p>

  <h2 class="abs welcome-title">Welcome to <strong>Corvane</strong></h2>
  <p class="abs welcome-text">Lorem Ipsum is simply dummy text of the printing and typesetting industry. Lorem Ipsum has been the industry's standard dummy text ever since the 1500s, when an unknown printer took a galley of type and scrambled it to make a type specimen book. It has survived not only five centuries, but also the leap into electronic typesetting, remaining essentially unchanged.</p>
  <a class="abs btn-about" href="#">ABOUT US</a>

  <div class="abs divider" style="top:1081px"></div>
  <div class="abs social-circle"></div>
  <p class="abs tweet-meta">Martin Ellery @CorvaneFarmers &nbsp;May 5</p>
  <p class="abs tweet-body">TOM ASHBY NEEDS YOUR HELP FIGHTING FOR FOOD EDUCATION <a href="#">#FoodFuturesDay https://www.petitionhub.org/p/tom-ashby</a></p>
  <div class="abs divider" style="top:1159px"></div>
  <p class="abs copyright">Copyright © 2015 Corvane. All Right Reserved.</p>
</body>
</html>
```